Business Consulting Business Card

professional business card with basic information (1) First and Last name (2) email address, (3) phone number, (4) website.

```html
<!DOCTYPE html>
<html lang="en">
<head>
<meta charset="utf-8">
<title>Tide Harbor – Business Card</title>
<link href="https://fonts.googleapis.com/css2?family=Montserrat:wght@600&family=Open+Sans:wght@400;600&display=swap" rel="stylesheet">
<style>
  :root {
    --navy: #0b2a42;
    --teal: #4fbdc5;
    --white: #ffffff;
    --map: #f2f3f4;
    --stage: #3e5a62;
  }
  * { box-sizing: border-box; margin: 0; padding: 0; }
  html, body { width: 1200px; height: 900px; overflow: hidden; }
  body {
    background: var(--stage);
    position: relative;
    font-family: "Open Sans", sans-serif;
    color: var(--navy);
  }
  .card {
    position: absolute;
    width: 600px;
    height: 345px;
    background: var(--white);
    border-radius: 18px;
    overflow: hidden;
    box-shadow: 0 10px 30px rgba(0,0,0,0.25);
  }
  .card--front { left: 80px; top: 90px; }
  .card--back { left: 520px; top: 465px; }

  .map-backdrop {
    position: absolute;
    inset: 0;
    background: linear-gradient(160deg, var(--white) 0%, var(--map) 100%);
  }

  .brand {
    position: absolute;
    display: flex;
    align-items: center;
    gap: 16px;
  }
  .brand__dot {
    border-radius: 50%;
    background: var(--teal);
    flex: none;
  }
  .brand__name {
    font-family: "Montserrat", sans-serif;
    font-weight: 600;
    color: var(--navy);
    letter-spacing: 0.32em;
    white-space: nowrap;
  }

  /* Front */
  .card--front .brand { left: 0; right: 0; top: 120px; justify-content: center; }
  .card--front .brand__dot { width: 48px; height: 48px; }
  .card--front .brand__name { font-size: 34px; }
  .front-band {
    position: absolute;
    left: 0; right: 0;
    top: 252px;
    height: 64px;
    background: var(--navy);
    display: flex;
    align-items: center;
    justify-content: center;
    color: var(--white);
    font-size: 17px;
    letter-spacing: 0.02em;
  }
  .front-stripe {
    position: absolute;
    left: 0; right: 0; bottom: 0;
    height: 29px;
    background: var(--teal);
  }

  /* Back */
  .back-shapes { position: absolute; inset: 0; }
  .back-tab {
    position: absolute;
    right: 0; top: 22px;
    width: 12px; height: 44px;
    background: var(--navy);
  }
  .person {
    position: absolute;
    right: 40px; top: 30px;
    text-align: right;
  }
  .person__name { font-size: 30px; color: var(--teal); line-height: 1.1; }
  .person__title { font-size: 17px; color: var(--navy); }

  .card--back .brand { left: 44px; top: 110px; gap: 12px; }
  .card--back .brand__dot { width: 38px; height: 38px; }
  .card--back .brand__name { font-size: 24px; }

  .contact-list {
    position: absolute;
    left: 56px; top: 166px;
    list-style: none;
    font-size: 15px;
    color: var(--navy);
  }
  .contact-list li {
    display: flex;
    align-items: center;
    gap: 12px;
    height: 24px;
  }
  .contact-list svg { width: 14px; height: 14px; flex: none; }

  .social {
    position: absolute;
    right: 40px; top: 226px;
    width: 190px;
    text-align: center;
    color: var(--white);
  }
  .social__label { font-size: 10px; font-weight: 600; letter-spacing: 0.04em; }
  .social__links { display: flex; justify-content: center; gap: 14px; margin-top: 10px; }
  .social__link {
    width: 32px; height: 32px;
    border: 2px solid var(--white);
    border-radius: 50%;
  }
</style>
</head>
<body>

  <section class="card card--front" aria-label="Business card front">
    <div class="map-backdrop" role="img" aria-label="Faint light grey world map in the background"></div>
    <div class="brand">
      <span class="brand__dot"></span>
      <span class="brand__name">TIDE HARBOR</span>
    </div>
    <div class="front-band">www.tideharborco.com</div>
    <div class="front-stripe"></div>
  </section>

  <section class="card card--back" aria-label="Business card back">
    <div class="map-backdrop" role="img" aria-label="Faint light grey world map in the background"></div>
    <svg class="back-shapes" viewBox="0 0 600 345" preserveAspectRatio="none" aria-hidden="true">
      <rect x="0" y="268" width="360" height="24" fill="var(--navy)"/>
      <path d="M0 292 H328 C343 292 350 282 350 266 V248 C350 226 366 212 392 212 H600 V345 H0 Z" fill="var(--teal)"/>
    </svg>
    <div class="back-tab"></div>

    <div class="person">
      <p class="person__name">Marlow Hayes</p>
      <p class="person__title">CEO/Founder</p>
    </div>

    <div class="brand">
      <span class="brand__dot"></span>
      <span class="brand__name">TIDE HARBOR</span>
    </div>

    <ul class="contact-list">
      <li>
        <svg viewBox="0 0 24 24"><path fill="var(--teal)" d="M6.6 10.8a15 15 0 0 0 6.6 6.6l2.2-2.2c.3-.3.7-.4 1-.2 1.1.4 2.3.6 3.6.6.6 0 1 .4 1 1V20c0 .6-.4 1-1 1A17 17 0 0 1 3 4c0-.6.4-1 1-1h3.5c.6 0 1 .4 1 1 0 1.3.2 2.5.6 3.6.1.3 0 .7-.2 1z"/></svg>
        +012-555-0142
      </li>
      <li>
        <svg viewBox="0 0 24 24"><path fill="var(--teal)" d="M2 11 22 2 15 22l-3-8z"/></svg>
        info@tideharborco.com
      </li>
      <li>
        <svg viewBox="0 0 24 24"><circle cx="12" cy="12" r="10" fill="none" stroke="var(--teal)" stroke-width="2"/><path d="M2 12h20M12 2c3 3 3 17 0 20M12 2c-3 3-3 17 0 20" fill="none" stroke="var(--teal)" stroke-width="2"/></svg>
        www.tideharborco.com
      </li>
      <li>
        <svg viewBox="0 0 24 24"><path fill="var(--teal)" d="M12 2a7 7 0 0 0-7 7c0 5 7 13 7 13s7-8 7-13a7 7 0 0 0-7-7zm0 9.5A2.5 2.5 0 1 1 12 6.5a2.5 2.5 0 0 1 0 5z"/></svg>
        Address, Suit, City, Country, Zip
      </li>
    </ul>

    <div class="social">
      <p class="social__label">FIND US ON SOCIAL MEDIA</p>
      <div class="social__links">
        <span class="social__link" aria-label="Social profile"></span>
        <span class="social__link" aria-label="Social profile"></span>
        <span class="social__link" aria-label="Social profile"></span>
      </div>
    </div>
  </section>

</body>
</html>
```